Marketing material for IT Company
Brochure/Sales Sheet/Flyer
Brochure will be in two languages, and tri-fold. Would go like this; front (outer) side: first fold: page for information in 2nd languge, second fold: page for information in 2nd language, third fold: cover page in 1st language; back side (inner) side: first fold is for information in 1st language, second fold is for information in 1st language, third fold is cover page for 2nd language.
Information Technology
Brochure view and dimensions are in an uploaded file. Size of flyer equals to size of 1 fold of brochure (i.e one brochure size = 3 flyers size). Size of Sales Sheet is equal to brochure's size. (Sales Sheet won't be folded).
Trifold Brochure view and dimensions
Tulmori logo and Divisions logos (CMYK)
Tulmori logo and Divisions logos (PMS)
Tulmori vertical logo and Divisions vertical logos (CMYK)
Tulmori vertical logo and Divisions vertical logos (PMS)
Tulmori old Brochure (uploaded as an example)
Example of our folder, if it can help
Example of our biz card, if it can help
To help you understand how we see our brochure, one more PIC
Tulmori logo colors information

```html
<!DOCTYPE html>
<html lang="en">
<head>
<meta charset="utf-8">
<title>Tulmori Tri-fold Brochure</title>
<link href="https://fonts.googleapis.com/css2?family=Open+Sans:wght@400;600;700&display=swap" rel="stylesheet">
<style>
  :root {
    --canvas: #e4e4e4;
    --paper: #ffffff;
    --paper-soft: #f3f4f6;
    --ink: #555a60;
    --ink-light: #8a8f95;
    --blue: #2e8fd0;
    --green: #5bb33a;
    --yellow: #f2b705;
    --orange: #ef6a2a;
    --red: #e03a3a;
    --purple: #8e4fb8;
    --photo-office: linear-gradient(135deg, #c9b79c 0%, #e8e2d6 45%, #9aa6ae 100%);
    --photo-hand: linear-gradient(160deg, #eef1f4 0%, #d9dde2 60%, #c6b7a6 100%);
    --photo-team: linear-gradient(135deg, #b08a6a 0%, #dcd1c3 55%, #6e7f8e 100%);
  }
  * { box-sizing: border-box; margin: 0; padding: 0; }
  html, body { width: 1200px; height: 497px; overflow: hidden; }
  body {
    background: var(--canvas);
    font-family: "Open Sans", Arial, sans-serif;
    color: var(--ink);
    position: relative;
  }
  .brochure {
    position: absolute;
    top: 6px;
    height: 485px;
    background: var(--paper);
    display: grid;
    grid-template-columns: 1fr 1fr 1fr;
    grid-template-rows: 206px 92px 1fr;
    box-shadow: 0 1px 4px rgba(0,0,0,0.18);
    overflow: hidden;
  }
  .brochure--first { left: 8px; width: 634px; }
  .brochure--second { left: 652px; width: 540px; }

  .panel { padding: 12px 14px 8px; position: relative; }
  .panel + .panel { border-left: 1px solid #eceef0; }

  .division { display: flex; align-items: center; gap: 6px; margin-bottom: 8px; }
  .division__dot { width: 16px; height: 16px; border-radius: 50%; flex: none; }
  .division__name { font-size: 13px; font-weight: 700; line-height: 1; color: var(--ink); }
  .division__sub { font-size: 8px; font-weight: 600; line-height: 1; margin-top: 2px; }

  .copy { font-size: 6.2px; line-height: 1.55; color: var(--ink-light); margin-bottom: 6px; }
  .bullets { list-style: none; }
  .bullets li {
    font-size: 6.2px; line-height: 1.55; color: var(--ink-light);
    padding-left: 8px; position: relative; margin-bottom: 3px;
  }
  .bullets li::before {
    content: ""; position: absolute; left: 0; top: 3px;
    width: 3px; height: 3px; border-radius: 50%; background: var(--ink-light);
  }

  .cover {
    grid-column: 3; grid-row: 1 / 3;
    background: var(--photo-hand);
    display: flex; flex-direction: column; align-items: center;
    padding-top: 14px; border-left: 1px solid #eceef0;
  }
  .cover__mark { width: 44px; height: 44px; border-radius: 50%; background: var(--blue); }
  .cover__name { font-size: 22px; font-weight: 600; color: var(--ink); margin-top: 6px; letter-spacing: 0.5px; }
  .cover__tagline { font-size: 13px; font-weight: 600; color: var(--blue); margin-top: 44px; align-self: flex-start; padding-left: 14px; }

  .photo-band {
    grid-column: 1 / 3; grid-row: 2;
    display: flex;
  }
  .photo-band__office { flex: 1.55; background: var(--photo-office); }
  .photo-band__frame {
    flex: 1; margin: 8px 6px 4px 8px;
    border: 4px solid var(--blue); border-radius: 4px;
    background: var(--photo-team);
  }
  .cover-frames {
    grid-column: 3; grid-row: 2 / 4;
    display: grid; grid-template-columns: 1fr 1fr; gap: 6px;
    padding: 26px 12px 0; align-content: start;
    z-index: 1;
  }
  .cover-frames__item { height: 62px; border: 3px solid; border-radius: 4px; background: var(--photo-team); }
  .cover-frames__item--green { border-color: var(--green); }
  .cover-frames__item--orange { border-color: var(--orange); }
  .cover-frames__item--purple { border-color: var(--purple); }
  .cover-frames__item--yellow { border-color: var(--yellow); }

  .lower { grid-row: 3; padding-top: 14px; }
  .lower--sales { grid-column: 1; }
  .lower--services { grid-column: 2; }

  .back-footer {
    grid-column: 3; grid-row: 3;
    display: flex; flex-direction: column; align-items: center; justify-content: flex-end;
    padding-bottom: 14px;
  }
  .back-footer__url { font-size: 7px; font-weight: 700; color: var(--ink); margin-bottom: 6px; }
  .swatches { display: flex; gap: 3px; }
  .swatches span { width: 9px; height: 9px; }
</style>
</head>
<body>

<section class="brochure brochure--first">
  <div class="panel">
    <div class="division"><span class="division__dot" style="background:var(--blue)"></span><div><div class="division__name">tulmori</div><div class="division__sub" style="color:var(--blue)">solutions</div></div></div>
    <p class="copy">We design, deploy and support complete IT solutions that keep your business running smoothly every day.</p>
    <ul class="bullets"><li>Network design and secure infrastructure</li><li>Software licensing and system integration</li><li>Data backup and recovery planning</li></ul>
  </div>
  <div class="panel">
    <div class="division"><span class="division__dot" style="background:var(--green)"></span><div><div class="division__name">tulmori</div><div class="division__sub" style="color:var(--green)">services</div></div></div>
    <p class="copy">Our service team offers fast, friendly help on site and remote, with clear plans for every budget.</p>
    <ul class="bullets"><li>Helpdesk support around the clock</li><li>Preventive maintenance and audits</li></ul>
  </div>
  <div class="cover" role="img" aria-label="Photo of a hand touching a screen">
    <span class="cover__mark"></span>
    <span class="cover__name">tulmori</span>
    <span class="cover__tagline">We Can Help!</span>
  </div>
  <div class="photo-band">
    <div class="photo-band__office" role="img" aria-label="Photo of a smiling man in a modern office"></div>
    <div class="photo-band__frame" role="img" aria-label="Photo of hands on a laptop keyboard"></div>
  </div>
  <div class="cover-frames">
    <div class="cover-frames__item cover-frames__item--green" role="img" aria-label="Photo of a woman on the phone"></div>
    <div class="cover-frames__item cover-frames__item--orange" role="img" aria-label="Photo of a team at a desk"></div>
    <div class="cover-frames__item cover-frames__item--purple" role="img" aria-label="Photo of colleagues meeting"></div>
    <div class="cover-frames__item cover-frames__item--yellow" role="img" aria-label="Photo of a technician at work"></div>
  </div>
  <div class="panel lower lower--sales">
    <div class="division"><span class="division__dot" style="background:var(--yellow)"></span><div><div class="division__name">tulmori</div><div class="division__sub" style="color:var(--yellow)">sales</div></div></div>
    <p class="copy">Our sales team helps you choose the right hardware and software at fair prices for your needs.</p>
    <ul class="bullets"><li>Servers, desktops and laptops</li><li>Printers and office equipment</li></ul>
  </div>
  <div class="panel lower lower--services">
    <div class="division"><span class="division__dot" style="background:var(--orange)"></span><div><div class="division__name">tulmori</div><div class="division__sub" style="color:var(--orange)">support</div></div></div>
    <p class="copy">From first call to final setup we stay with you, training your staff and tuning every system.</p>
    <ul class="bullets"><li>Installation and setup</li><li>Staff training sessions</li></ul>
  </div>
  <div class="back-footer">
    <span class="back-footer__url">www.lorvex.net</span>
    <div class="swatches"><span style="background:var(--blue)"></span><span style="background:var(--green)"></span><span style="background:var(--yellow)"></span><span style="background:var(--orange)"></span><span style="background:var(--red)"></span><span style="background:var(--purple)"></span></div>
  </div>
</section>

<section class="brochure brochure--second">
  <div class="panel">
    <div class="division"><span class="division__dot" style="background:var(--blue)"></span><div><div class="division__name">tulmori</div><div class="division__sub" style="color:var(--blue)">solutions</div></div></div>
    <p class="copy">We design, deploy and support complete IT solutions that keep your business running smoothly every day.</p>
    <ul class="bullets"><li>Network design and secure infrastructure</li><li>Software licensing and system integration</li><li>Data backup and recovery planning</li></ul>
  </div>
  <div class="panel">
    <div class="division"><span class="division__dot" style="background:var(--green)"></span><div><div class="division__name">tulmori</div><div class="division__sub" style="color:var(--green)">services</div></div></div>
    <p class="copy">Our service team offers fast, friendly help on site and remote, with clear plans for every budget.</p>
    <ul class="bullets"><li>Helpdesk support around the clock</li><li>Preventive maintenance and audits</li></ul>
  </div>
  <div class="cover" role="img" aria-label="Photo of a hand touching a screen">
    <span class="cover__mark"></span>
    <span class="cover__name">tulmori</span>
    <span class="cover__tagline">We Can Help!</span>
  </div>
  <div class="photo-band">
    <div class="photo-band__office" role="img" aria-label="Photo of a smiling man in a modern office"></div>
    <div class="photo-band__frame" role="img" aria-label="Photo of hands on a laptop keyboard"></div>
  </div>
  <div class="cover-frames">
    <div class="cover-frames__item cover-frames__item--green" role="img" aria-label="Photo of a woman on the phone"></div>
    <div class="cover-frames__item cover-frames__item--orange" role="img" aria-label="Photo of a team at a desk"></div>
    <div class="cover-frames__item cover-frames__item--purple" role="img" aria-label="Photo of colleagues meeting"></div>
    <div class="cover-frames__item cover-frames__item--yellow" role="img" aria-label="Photo of a technician at work"></div>
  </div>
  <div class="panel lower lower--sales">
    <div class="division"><span class="division__dot" style="background:var(--yellow)"></span><div><div class="division__name">tulmori</div><div class="division__sub" style="color:var(--yellow)">sales</div></div></div>
    <p class="copy">Our sales team helps you choose the right hardware and software at fair prices for your needs.</p>
    <ul class="bullets"><li>Servers, desktops and laptops</li><li>Printers and office equipment</li></ul>
  </div>
  <div class="panel lower lower--services">
    <div class="division"><span class="division__dot" style="background:var(--orange)"></span><div><div class="division__name">tulmori</div><div class="division__sub" style="color:var(--orange)">support</div></div></div>
    <p class="copy">From first call to final setup we stay with you, training your staff and tuning every system.</p>
    <ul class="bullets"><li>Installation and setup</li><li>Staff training sessions</li></ul>
  </div>
  <div class="back-footer">
    <span class="back-footer__url">www.lorvex.net</span>
    <div class="swatches"><span style="background:var(--blue)"></span><span style="background:var(--green)"></span><span style="background:var(--yellow)"></span><span style="background:var(--orange)"></span><span style="background:var(--red)"></span><span style="background:var(--purple)"></span></div>
  </div>
</section>

</body>
</html>
```